Small rum distillery looking for bottle design

Small rum distillery in Estonia. Looking for bottle lable design. It should be simple but at the same time point out from the variety of other bottles.
As we are a small nordic country, design can be some how nordic or represent our country. It can also have some connection with sailing or sea as we know it pirates love it.
Bottle we are using is Corvane 540

Industry/Entity Type

food and beverage

Other font styles liked:
• Baskerville

```html
<!DOCTYPE html>
<html lang="en">
<head>
<meta charset="utf-8">
<title>Varsk Distillery – Rum Label Variants</title>
<link href="https://fonts.googleapis.com/css2?family=Libre+Baskerville:wght@400&display=swap" rel="stylesheet">
<style>
  :root {
    --page-bg: #f6f1f1;
    --ink: #ffffff;
    --red-outer: #8a2e2f;
    --red-arch: #a4383b;
    --red-art: #b85558;
    --grey-outer: #4a4a4a;
    --grey-arch: #575757;
    --grey-art: #6c6c6c;
  }
  * { margin: 0; padding: 0; box-sizing: border-box; }
  html, body {
    width: 979px;
    height: 1200px;
    overflow: hidden;
    background: var(--page-bg);
  }
  .canvas {
    width: 979px;
    height: 1200px;
    display: flex;
    align-items: center;
    justify-content: center;
    gap: 33px;
  }
  .label {
    width: 440px;
    height: 546px;
    display: block;
    box-shadow: 0 4px 14px rgba(0,0,0,0.08);
  }
  .label--red { --outer: var(--red-outer); --arch: var(--red-arch); --art: var(--red-art); }
  .label--grey { --outer: var(--grey-outer); --arch: var(--grey-arch); --art: var(--grey-art); }
  .label__ground { fill: var(--outer); }
  .label__arch { fill: var(--arch); }
  .label__frame { fill: none; stroke: var(--ink); stroke-width: 4; }
  .label__artwork { fill: var(--art); }
  .label__badge { fill: none; stroke: var(--ink); stroke-width: 3; }
  .label__rule { stroke: var(--ink); stroke-width: 2; }
  .label__name {
    fill: var(--ink);
    font-family: "Libre Baskerville", Baskerville, serif;
    font-size: 50px;
    letter-spacing: 1px;
  }
  .label__tagline {
    fill: var(--ink);
    font-family: "Libre Baskerville", Baskerville, serif;
    font-size: 15px;
    letter-spacing: 6px;
  }
</style>
</head>
<body>
<main class="canvas">
  <svg class="label label--red" viewBox="0 0 466 578" aria-label="Varsk Distillery label, red">
    <rect class="label__ground" x="0" y="0" width="466" height="578"/>
    <path class="label__arch" d="M56 553 V202 A182 182 0 0 1 420 202 V553 Z"/>
    <path class="label__frame" d="M73 536 V198 A161 161 0 0 1 395 198 V536 Z"/>
    <g role="img" aria-label="Illustration of a pirate skull in a tricorn hat over crossed cutlasses">
      <rect class="label__artwork" x="133" y="88" width="200" height="250" rx="10"/>
    </g>
    <circle class="label__badge" cx="233" cy="362" r="28"/>
    <text class="label__name" x="233" y="450" text-anchor="middle">VARSK</text>
    <line class="label__rule" x1="135" y1="466" x2="331" y2="466"/>
    <text class="label__tagline" x="236" y="489" text-anchor="middle">DISTILLERY</text>
  </svg>

  <svg class="label label--grey" viewBox="0 0 466 578" aria-label="Varsk Distillery label, charcoal">
    <rect class="label__ground" x="0" y="0" width="466" height="578"/>
    <path class="label__arch" d="M56 553 V202 A182 182 0 0 1 420 202 V553 Z"/>
    <path class="label__frame" d="M73 536 V198 A161 161 0 0 1 395 198 V536 Z"/>
    <g role="img" aria-label="Illustration of a pirate skull in a tricorn hat over crossed cutlasses">
      <rect class="label__artwork" x="133" y="88" width="200" height="250" rx="10"/>
    </g>
    <circle class="label__badge" cx="233" cy="362" r="28"/>
    <text class="label__name" x="233" y="450" text-anchor="middle">VARSK</text>
    <line class="label__rule" x1="135" y1="466" x2="331" y2="466"/>
    <text class="label__tagline" x="236" y="489" text-anchor="middle">DISTILLERY</text>
  </svg>
</main>
</body>
</html>
```